Need Business Cards for my Business

email address: rkpmarlowhollowworks@vendrimail.com
web address: rkpmarlowhollowworks.net
Slogan: We offer various QVN licenses
Rowland K. Pemberly
Please stick with colors of Company Logo
would like the card to be more of the color example of the logo.
If you need PDF copy of logo email me at the above account.
Creative control rests with you.

Industry/Entity Type

Business

Contact Information for Business Card

I am a minimalist, but would like something to pop and stand out amongst other cards, make it memorable.

Font styles to use
Serif
Decorative
Script

```html
<!DOCTYPE html>
<html lang="en">
<head>
<meta charset="utf-8">
<title>RKP Marlow Hollow Works – Business Cards</title>
<link rel="stylesheet" href="https://fonts.googleapis.com/css2?family=Exo+2:wght@400;700&display=swap">
<style>
  :root {
    --bg: #e9e6e1;
    --card: #f7f7f5;
    --navy: #1c2a44;
    --blue: #13508f;
    --blue-dark: #0d3a6c;
    --red: #d41f28;
    --red-dark: #b5161f;
    --ink: #1e2430;
    --frame: #c9c9c9;
  }
  * { box-sizing: border-box; margin: 0; padding: 0; }
  html, body { width: 1200px; height: 800px; overflow: hidden; }
  body {
    background: var(--bg);
    font-family: "Exo 2", sans-serif;
    color: var(--ink);
    position: relative;
  }
  .card {
    position: absolute;
    width: 560px;
    height: 320px;
    background: var(--card);
    box-shadow: 0 6px 18px rgba(0,0,0,0.18);
    overflow: hidden;
  }
  /* Front */
  .card-front { left: 60px; top: 60px; }
  .card-front .frame {
    position: absolute; inset: 14px;
    border: 1px solid var(--frame);
    border-radius: 6px;
  }
  .card-front .tab-top {
    position: absolute; top: 0; left: 150px;
    width: 370px; height: 46px;
    background: linear-gradient(180deg, var(--blue-dark), var(--blue));
    border-radius: 0 0 18px 18px;
  }
  .card-front .tab-bottom {
    position: absolute; bottom: 0; left: 225px;
    width: 270px; height: 60px;
    background: linear-gradient(180deg, var(--red), var(--red-dark));
    border-radius: 18px 18px 0 0;
  }
  .card-front .brand {
    position: absolute; left: 62px; top: 118px;
    display: flex; align-items: center; gap: 20px;
  }
  .brand-mark { width: 44px; height: 44px; background: var(--red); flex: none; }
  .card-front .brand-name {
    font-size: 30px; font-weight: 700; letter-spacing: 1px;
    color: var(--navy); line-height: 1.05; text-transform: uppercase;
  }
  .card-front .site {
    position: absolute; left: 0; right: 0; bottom: 74px;
    text-align: center; font-size: 15px; letter-spacing: 0.5px;
  }
  /* Back */
  .card-back { left: 580px; top: 420px; }
  .card-back .panels { position: absolute; left: 0; top: 0; width: 560px; height: 320px; }
  .card-back .info { position: absolute; left: 258px; top: 36px; right: 14px; }
  .card-back .brand { display: flex; align-items: center; gap: 10px; margin-bottom: 26px; }
  .card-back .brand-mark { width: 28px; height: 28px; }
  .card-back .brand-name {
    font-size: 16px; font-weight: 700; color: var(--navy);
    text-transform: uppercase; line-height: 1.1; white-space: nowrap;
  }
  .person { font-size: 22px; font-weight: 700; color: var(--navy); white-space: nowrap; }
  .slogan { font-size: 14px; margin-top: 4px; margin-bottom: 22px; white-space: nowrap; }
  .contact { list-style: none; }
  .contact li {
    display: flex; align-items: center; gap: 10px;
    font-size: 12px; margin-bottom: 8px; white-space: nowrap;
  }
  .icon {
    width: 28px; height: 28px; flex: none;
    display: flex; align-items: center; justify-content: center;
  }
  .icon-mail { background: var(--red); }
  .icon-web { background: var(--blue); }
</style>
</head>
<body>

<section class="card card-front">
  <div class="frame"></div>
  <div class="tab-top"></div>
  <div class="brand">
    <span class="brand-mark"></span>
    <span class="brand-name">RKP Marlow<br>Hollow Works</span>
  </div>
  <p class="site">www.rkpmarlowhollowworks.net</p>
  <div class="tab-bottom"></div>
</section>

<section class="card card-back">
  <svg class="panels" viewBox="0 0 560 320" aria-hidden="true">
    <polygon points="0,70 0,320 300,320 215,205 130,130" fill="#13508f"/>
    <polygon points="0,70 100,48 112,150 65,172 0,160" fill="#d41f28"/>
    <polygon points="108,46 190,30 228,56 240,128 212,170 150,172 114,150" fill="#1c2a44"/>
    <polygon points="95,190 115,168 200,165 218,192 225,320 115,320 95,290" fill="#d41f28"/>
    <polygon points="0,175 70,185 90,200 92,320 0,320" fill="#0d3a6c"/>
  </svg>
  <div class="info">
    <div class="brand">
      <span class="brand-mark"></span>
      <span class="brand-name">RKP Marlow Hollow Works</span>
    </div>
    <p class="person">Rowland K. Pemberly</p>
    <p class="slogan">We offer various QVN licenses</p>
    <ul class="contact">
      <li>
        <span class="icon icon-mail">
          <svg width="16" height="12" viewBox="0 0 16 12" aria-hidden="true"><rect x="0.5" y="0.5" width="15" height="11" fill="#fff"/><polyline points="0.5,0.5 8,7 15.5,0.5" fill="none" stroke="#d41f28" stroke-width="1.2"/></svg>
        </span>
        rkpmarlowhollowworks@vendrimail.com
      </li>
      <li>
        <span class="icon icon-web">
          <svg width="16" height="16" viewBox="0 0 16 16" aria-hidden="true"><g fill="none" stroke="#fff" stroke-width="1.2"><circle cx="8" cy="8" r="7"/><ellipse cx="8" cy="8" rx="3" ry="7"/><line x1="1" y1="8" x2="15" y2="8"/></g></svg>
        </span>
        www.rkpmarlowhollowworks.net
      </li>
    </ul>
  </div>
</section>

</body>
</html>
```